Software static HTML page design

We need 5 static HTML pages designed for our current software startup - TallyNest. All details are attached in a document for consideration.

Target Market(s)

Sporting clubs/University clubs

Industry/Entity Type

Software

Number of Pages Required

5+ page

Font styles to use
Sans Serif

Colors
33a6d7
85cae6
86cfc6
33b8a4
ffffff

```html
<!DOCTYPE html>
<html lang="en">
<head>
<meta charset="utf-8">
<title>TallyNest – Bringing your club to the social web</title>
<link href="https://fonts.googleapis.com/css2?family=Lato:wght@400;700&family=Open+Sans:wght@400;600;700&family=Alegreya+Sans:wght@400;500&display=swap" rel="stylesheet">
<style>
:root{
  --blue:#33a6d7;
  --sky:#85cae6;
  --mint:#86cfc6;
  --teal:#33b8a4;
  --white:#ffffff;
  --ink:#222222;
  --text:#555555;
  --muted:#8a8a8a;
  --bar:#2b2a2b;
  --bar-deep:#1b1b1b;
  --soft:#f6f6f6;
  --price-bg:#eaf2fa;
  --price-band:#5b9fd6;
}
*{box-sizing:border-box;margin:0;padding:0}
html,body{width:1200px;height:2765px;overflow:hidden}
body{position:relative;background:var(--white);font-family:'Lato',sans-serif;color:var(--text)}
.abs{position:absolute}

/* top bar */
.topbar{left:0;top:0;width:1200px;height:26px;background:var(--bar)}
.topbar .account{left:66px;top:5px;font-size:12px;color:var(--white);display:flex;gap:18px;align-items:center}
.topbar .account span{display:flex;align-items:center;gap:6px}
.topbar .account .sep{width:1px;height:14px;background:#777}
.topbar .social{left:1017px;top:8px;display:flex;gap:11px}
.dot{width:10px;height:10px;border-radius:50%;background:#cfcfcf}

/* header */
.header{left:0;top:26px;width:1200px;height:99px;background:var(--white)}
.brand{left:68px;top:28px;display:flex;align-items:center;gap:10px}
.brand-mark{width:34px;height:34px;background:var(--blue);border-radius:3px}
.brand-name{font-weight:700;font-size:30px;color:var(--blue);letter-spacing:.5px}
.nav{top:38px;font-size:13px;font-weight:700;color:#444;letter-spacing:.5px}

/* hero */
.hero{left:0;top:125px;width:1200px;height:492px;background:linear-gradient(100deg,#f2f2f2 0%,#f7f7f4 45%,#eef5ee 100%)}
.hero-art{left:0;top:0;width:820px;height:492px;background:linear-gradient(125deg,rgba(229,70,120,.55),rgba(240,120,100,.5) 35%,rgba(110,180,110,.4) 60%,rgba(240,240,240,0) 85%)}
.hero-phone{left:720px;top:15px;width:480px;height:477px;background:radial-gradient(circle at 55% 45%,rgba(120,200,230,.55),rgba(240,245,240,0) 70%)}
.hero h1{left:0;top:152px;width:1200px;text-align:center;font-family:'Open Sans',sans-serif;font-weight:600;font-size:55px;line-height:62px;color:var(--ink)}
.btn-hero{left:520px;top:327px;width:166px;height:40px;background:var(--blue);color:var(--white);font-family:'Open Sans',sans-serif;font-weight:600;font-size:16px;line-height:40px;text-align:center;border-radius:3px;box-shadow:0 3px 0 #1f6f93}

/* intro */
.intro{left:0;top:617px;width:1200px;height:631px;background:var(--soft)}
.intro h2{left:66px;top:62px;width:560px;font-family:'Open Sans',sans-serif;font-weight:400;font-size:27px;line-height:37px;color:var(--ink)}
.intro p{left:64px;top:172px;width:590px;font-size:19.5px;line-height:31px;color:#777}
.btn-learn{left:68px;top:441px;width:264px;height:52px;background:var(--mint);color:var(--white);font-weight:700;font-size:20px;letter-spacing:1px;line-height:52px;text-align:center;border-radius:3px}
.intro-art{left:650px;top:-60px;width:550px;height:660px;background:linear-gradient(160deg,#ffffff 0%,#e4f3f9 45%,#fbe3da 100%);border-radius:26px}

/* features */
.features{left:0;top:1248px;width:1200px;height:420px;background:var(--white)}
.section-title{width:1200px;left:0;text-align:center;font-family:'Open Sans',sans-serif;font-weight:400;font-size:31px;color:#333;letter-spacing:.5px}
.feature{top:0;width:240px;text-align:center}
.feature .icon{width:125px;height:125px;border-radius:50%;background:#f0f0f0;border:6px solid #e6e6e6;margin:87px auto 0;display:flex;align-items:center;justify-content:center}
.feature h3{margin-top:22px;font-size:15px;font-weight:700;color:var(--ink)}
.feature p{margin-top:14px;font-size:13px;line-height:24px;color:#444}

/* pricing */
.pricing{left:0;top:1668px;width:1200px;height:584px;background:var(--price-bg)}
.plan{top:122px;width:319px;height:379px;background:var(--white)}
.plan h3{margin-top:24px;text-align:center;font-family:'Alegreya Sans',sans-serif;font-weight:400;font-size:30px;color:var(--ink)}
.plan .tag{text-align:center;font-size:12px;color:var(--muted);margin-top:2px}
.plan .band{margin-top:14px;height:70px;background:var(--price-band);color:var(--white);display:flex;align-items:center;justify-content:center;gap:6px}
.plan .band b{font-family:'Open Sans',sans-serif;font-weight:700;font-size:38px}
.plan .band small{font-size:12px;margin-top:12px}
.plan ul{list-style:none;margin:18px 0 0 70px}
.plan li{font-size:14px;line-height:28px;color:#444;display:flex;align-items:center;gap:12px}
.plan li.off{color:#999;text-decoration:line-through}
.plan .buy{position:absolute;left:92px;top:315px;width:133px;height:37px;background:var(--price-band);color:var(--white);font-size:12px;font-weight:700;line-height:37px;text-align:center}

/* call to action */
.cta{left:0;top:2252px;width:1200px;height:164px;background:var(--white)}
.cta p{left:64px;top:38px;width:720px;font-family:'Open Sans',sans-serif;font-size:34px;line-height:44px;color:var(--teal)}
.btn-contact{left:942px;top:66px;width:190px;height:41px;background:var(--sky);color:var(--white);font-weight:700;font-size:21px;line-height:41px;text-align:center;border-radius:2px}

/* footer */
.footer{left:0;top:2416px;width:1200px;height:291px;background:var(--bar)}
.fcol{top:48px}
.fcol h4{font-size:13px;font-weight:700;color:var(--white);letter-spacing:.5px}
.fcol ul{list-style:none;margin-top:20px}
.fcol li{font-size:12.5px;line-height:28px;color:#e6e6e6}
.fsocial{display:flex;gap:13px;margin-top:32px}
.fsocial .dot{width:14px;height:14px;background:#e6e6e6}
.fsocial .dot.first{background:var(--blue)}
.copyright{left:0;top:2707px;width:1200px;height:58px;background:var(--bar-deep);color:var(--white);font-size:12px;text-align:center;line-height:58px}
</style>
</head>
<body>

<div class="abs topbar">
  <div class="abs account">
    <span><svg width="10" height="10" viewBox="0 0 10 10"><circle cx="5" cy="3" r="2.5" fill="#fff"/><path d="M0 10a5 4 0 0 1 10 0z" fill="#fff"/></svg>Login</span>
    <i class="sep"></i>
    <span><svg width="11" height="10" viewBox="0 0 11 10"><rect x="0.5" y="0.5" width="7" height="9" fill="none" stroke="#fff"/><path d="M4 5h7M9 3l2 2-2 2" stroke="#fff" fill="none"/></svg>signup</span>
  </div>
  <div class="abs social" role="img" aria-label="Social network links">
    <i class="dot"></i><i class="dot"></i><i class="dot"></i><i class="dot"></i><i class="dot"></i><i class="dot"></i>
  </div>
</div>

<header class="abs header">
  <div class="abs brand"><i class="brand-mark"></i><span class="brand-name">TallyNest</span></div>
  <nav>
    <span class="abs nav" style="left:848px">FEATURES</span>
    <span class="abs nav" style="left:962px">PRICING</span>
    <span class="abs nav" style="left:1065px">CONTACT</span>
  </nav>
</header>

<section class="abs hero">
  <div class="abs hero-art" role="img" aria-label="Colourful overlapping geometric shapes with scattered dots"></div>
  <div class="abs hero-phone" role="img" aria-label="Hand holding a smartphone surrounded by social app icons"></div>
  <h1 class="abs">Bringing your club to the<br>social web</h1>
  <a class="abs btn-hero">Find out more</a>
</section>

<section class="abs intro">
  <div class="abs intro-art" role="img" aria-label="Two phone screens showing a login form and a club dashboard with charts"></div>
  <h2 class="abs">Lorem ipsum dolor sit amet consectetur adipiscing elit. Nulla aliquam</h2>
  <p class="abs">Lorem ipsum dolor sit amet, consectetur adipiscing elit. Nulla aliquam tellus nisi. In lobortis ante nibh, lobortis ultrices arcu effi citur et. Mauris id turpis in dolor pulvinar venenatis hendrerit sed arcu. Vivamus ac odio volutpat, pharetra odio quis, venenatis eros. Aenean porta rutrum odio eget aliquet. Pellentesque habitant mor bi tristique senectus et netus et malesuada fames ac turpis egestas. Integer eu massa at urna suscipit dapibus sed et nibh.</p>
  <a class="abs btn-learn">LEARN MORE</a>
</section>

<section class="abs features">
  <h2 class="abs section-title" style="top:34px">FEATURES</h2>

  <div class="abs feature" style="left:77px">
    <div class="icon"><svg width="56" height="48" viewBox="0 0 56 48"><circle cx="20" cy="24" r="13" fill="none" stroke="#777" stroke-width="8" stroke-dasharray="5 3.2"/><circle cx="20" cy="24" r="5" fill="#777"/><circle cx="43" cy="12" r="7" fill="none" stroke="#777" stroke-width="5" stroke-dasharray="3 2.2"/><circle cx="43" cy="36" r="7" fill="none" stroke="#777" stroke-width="5" stroke-dasharray="3 2.2"/></svg></div>
    <h3>GREAT SUPPORT</h3>
    <p>Lorem ipsum dolor sit amet, consectet adipiscing elit. Etiam quis placerat urna. Nulla nulla diam, adipiscing non ornardfe non, commodo</p>
  </div>

  <div class="abs feature" style="left:344px">
    <div class="icon"><svg width="50" height="46" viewBox="0 0 50 46"><path d="M8 40C6 18 22 4 46 4c0 24-14 36-34 34z" fill="#777"/><path d="M4 44L30 18" stroke="#f0f0f0" stroke-width="3"/></svg></div>
    <h3>CLEAN &amp; SIMPLE</h3>
    <p>Lorem ipsum dolor sit amet, consectet adipiscing elit. Etiam quis placerat urna. Nulla nulla diam, adipiscing non ornardfe non, commodo</p>
  </div>

  <div class="abs feature" style="left:611px">
    <div class="icon"><svg width="50" height="50" viewBox="0 0 50 50"><path d="M13 4h24v12a12 12 0 0 1-24 0z" fill="#777"/><path d="M13 8H4c0 10 5 14 10 14M37 8h9c0 10-5 14-10 14" fill="none" stroke="#777" stroke-width="3"/><rect x="22" y="27" width="6" height="10" fill="#777"/><rect x="14" y="37" width="22" height="8" fill="#777"/></svg></div>
    <h3>CRISP LINE ICONS</h3>
    <p>Lorem ipsum dolor sit amet, consectet adipiscing elit. Etiam quis placerat urna. Nulla nulla diam, adipiscing non ornardfe non, commodo</p>
  </div>

  <div class="abs feature" style="left:877px">
    <div class="icon"><svg width="58" height="42" viewBox="0 0 58 42"><rect x="9" y="3" width="40" height="28" rx="2" fill="none" stroke="#777" stroke-width="4"/><path d="M2 35h54l-3 5H5z" fill="#777"/></svg></div>
    <h3>FULLY RESPONSIVE</h3>
    <p>Lorem ipsum dolor sit amet, consectet adipiscing elit. Etiam quis placerat urna. Nulla nulla diam, adipiscing non ornardfe non, commodo</p>
  </div>
</section>

<section class="abs pricing">
  <h2 class="abs section-title" style="top:34px">PRICING</h2>

  <div class="abs plan" style="left:94px">
    <h3>Basic</h3><div class="tag">Counciling Plan</div>
    <div class="band"><b>$350</b><small>/Per Month</small></div>
    <ul>
      <li><svg width="10" height="10" viewBox="0 0 10 10"><path d="M1 5l3 3 5-6" fill="none" stroke="#3aa655" stroke-width="2"/></svg>40 GB Data Limit</li>
      <li><svg width="10" height="10" viewBox="0 0 10 10"><path d="M1 5l3 3 5-6" fill="none" stroke="#3aa655" stroke-width="2"/></svg>Unlimited Band Width</li>
      <li class="off"><svg width="10" height="10" viewBox="0 0 10 10"><path d="M2 2l6 6M8 2l-6 6" stroke="#d9443a" stroke-width="2"/></svg>4MB Speed</li>
      <li class="off"><svg width="10" height="10" viewBox="0 0 10 10"><path d="M2 2l6 6M8 2l-6 6" stroke="#d9443a" stroke-width="2"/></svg>Free Instalation</li>
    </ul>
    <a class="buy">PURCHASE &nbsp;›</a>
  </div>

  <div class="abs plan" style="left:440px">
    <h3>Standard</h3><div class="tag">Business Plane</div>
    <div class="band"><b>$850</b><small>/Per Month</small></div>
    <ul>
      <li><svg width="10" height="10" viewBox="0 0 10 10"><path d="M1 5l3 3 5-6" fill="none" stroke="#3aa655" stroke-width="2"/></svg>200 GB Data Limit</li>
      <li><svg width="10" height="10" viewBox="0 0 10 10"><path d="M1 5l3 3 5-6" fill="none" stroke="#3aa655" stroke-width="2"/></svg>Unlimited Band Width</li>
      <li><svg width="10" height="10" viewBox="0 0 10 10"><path d="M1 5l3 3 5-6" fill="none" stroke="#3aa655" stroke-width="2"/></svg>12MB Speed</li>
      <li><svg width="10" height="10" viewBox="0 0 10 10"><path d="M1 5l3 3 5-6" fill="none" stroke="#3aa655" stroke-width="2"/></svg>Free Instalation</li>
    </ul>
    <a class="buy">PURCHASE &nbsp;›</a>
  </div>

  <div class="abs plan" style="left:787px">
    <h3>Ultimate</h3><div class="tag">Gold Plan</div>
    <div class="band"><b>$500</b><small>/Per Month</small></div>
    <ul>
      <li><svg width="10" height="10" viewBox="0 0 10 10"><path d="M1 5l3 3 5-6" fill="none" stroke="#3aa655" stroke-width="2"/></svg>100 GB Data Limit</li>
      <li><svg width="10" height="10" viewBox="0 0 10 10"><path d="M1 5l3 3 5-6" fill="none" stroke="#3aa655" stroke-width="2"/></svg>Unlimited Band Width</li>
      <li><svg width="10" height="10" viewBox="0 0 10 10"><path d="M1 5l3 3 5-6" fill="none" stroke="#3aa655" stroke-width="2"/></svg>8MB Speed</li>
      <li class="off"><svg width="10" height="10" viewBox="0 0 10 10"><path d="M2 2l6 6M8 2l-6 6" stroke="#d9443a" stroke-width="2"/></svg>Free Instalation</li>
    </ul>
    <a class="buy">PURCHASE &nbsp;›</a>
  </div>
</section>

<section class="abs cta">
  <p class="abs">Lorem ipsum dolor sit amet consectetur adipiscing elit Nulla</p>
  <a class="abs btn-contact">Contact</a>
</section>

<footer class="abs footer">
  <div class="abs fcol" style="left:77px"><h4>PRODUCTS</h4>
    <ul><li>Memberships</li><li>Season Passes</li><li>Team Sync</li><li>Fixtures</li><li>Rosters</li><li>Results</li></ul></div>
  <div class="abs fcol" style="left:293px"><h4>DEVELOPERS</h4>
    <ul><li>Documentation</li><li>API reference</li><li>API status</li><li>Open source</li></ul></div>
  <div class="abs fcol" style="left:523px"><h4>COMPANY</h4>
    <ul><li>About</li><li>Customers</li><li>Jobs</li><li>Blog</li><li>Press</li></ul></div>
  <div class="abs fcol" style="left:710px"><h4>RESOURCES</h4>
    <ul><li>Support</li><li>Contact</li><li>Privacy &amp; terms</li></ul></div>
  <div class="abs fcol" style="left:925px"><h4>FOLLOW US</h4>
    <div class="fsocial" role="img" aria-label="Social network links">
      <i class="dot first"></i><i class="dot"></i><i class="dot"></i><i class="dot"></i><i class="dot"></i><i class="dot"></i>
    </div></div>
</footer>
<div class="abs copyright">Copyright © . All Rights Reserved</div>

</body>
</html>
```